Childcare Centre trifold brochure

Design a contemporary trifold brochure for a childcare centre that meets Australian printing requirements with supplied content, logo's, fonts and photo's. Please refer to the attached DL flyer front and back for similar possible style and content.

Target Market(s)

Families

Industry/Entity Type

Childcare

Requirements
Must have
• refer attached content, photo's, logo's and examples. Colours should be same as Pantone purple and green and or variations of. Refer attached dl flyer example.

```html
<!DOCTYPE html>
<html lang="en">
<head>
<meta charset="utf-8">
<title>Bright Sprouts – Trifold Brochure</title>
<link href="https://fonts.googleapis.com/css2?family=Sniglet:wght@400;800&family=Delius&family=Open+Sans:wght@400;600;700&display=swap" rel="stylesheet">
<style>
  :root{
    --purple:#a80fbb;
    --purple-deep:#7d0a8c;
    --purple-dark:#650b72;
    --green:#22c01b;
    --green-dark:#159a10;
    --grey-light:#ececee;
    --grey-dark:#3d3d3d;
    --quote-grey:#cfcfcf;
    --badge-grey:#d8d8db;
    --white:#ffffff;
    --ink:#1e1e1e;
    --stage:#e4e4e6;
  }
  *{box-sizing:border-box;margin:0;padding:0}
  html,body{width:1200px;height:800px;overflow:hidden;background:var(--stage)}
  .brochure{position:absolute;left:48px;top:10px;width:1104px;height:780px;display:flex;box-shadow:0 6px 24px rgba(0,0,0,.18)}
  .panel{position:relative;width:368px;height:780px;overflow:hidden}
  .panel-bg{position:absolute;inset:0}
  .abs{position:absolute}

  /* left panel */
  .quote-mark{font-family:Georgia,serif;font-size:110px;color:var(--quote-grey);line-height:1}
  .quote-open{left:30px;top:40px}
  .quote-close{left:282px;top:262px}
  .quote-text{left:34px;top:130px;width:296px;font-family:"Delius",cursive;font-size:14px;line-height:1.4;color:var(--ink)}
  .quote-author{left:130px;top:290px;font-family:"Delius",cursive;font-size:18px;color:var(--purple)}
  .photo-pair{left:0;top:320px}
  .section-title{font-family:"Sniglet",cursive;font-weight:800;color:var(--white);font-size:26px;line-height:1.15}
  .title-rule{width:34px;height:4px;background:var(--green);margin:4px 0 10px}
  .curriculum{left:28px;top:530px;width:316px}
  .curriculum p{font-family:"Open Sans",sans-serif;font-size:9.5px;line-height:1.35;color:var(--white);margin-bottom:8px}

  /* middle panel */
  .badges{left:40px;top:62px;display:flex;gap:14px;align-items:center}
  .tagline{left:0;top:200px;width:368px;text-align:center;font-family:"Delius",cursive;font-size:30px;line-height:1.15;color:var(--green-dark)}
  .info{left:0;top:400px;width:368px;text-align:center;color:var(--white);font-family:"Sniglet",cursive}
  .info h2{font-weight:800;font-size:22px}
  .info .rule{width:34px;height:3px;background:var(--green);margin:6px auto 10px}
  .info .hours{font-size:15px;font-weight:800}
  .info .small{font-family:"Open Sans",sans-serif;font-size:10px;font-weight:700;margin-bottom:10px}
  .info .line{font-size:15px;font-weight:800;display:flex;justify-content:center;align-items:center;gap:6px}
  .social-dot{width:12px;height:12px;border-radius:50%;background:var(--white);display:inline-block}
  .enrol{font-size:32px;font-weight:800;margin-top:26px}
  .phone{font-size:22px;font-weight:800;display:flex;justify-content:center;align-items:center;gap:8px}
  .email{font-family:"Open Sans",sans-serif;font-size:13px;font-weight:700;margin-top:14px;display:flex;justify-content:center;align-items:center;gap:8px}
  .web{left:0;top:730px;width:368px;text-align:center;font-family:"Open Sans",sans-serif;font-size:15px;font-weight:700;color:var(--white);display:flex;justify-content:center;align-items:center;gap:8px}

  /* right panel */
  .brand{left:0;top:32px;width:368px;text-align:center}
  .brand-name{display:inline-flex;align-items:center;gap:10px;font-family:"Sniglet",cursive;font-weight:800;font-size:34px;color:var(--purple)}
  .brand-dot{width:20px;height:20px;border-radius:50%;background:var(--green)}
  .brand-sub{font-family:"Delius",cursive;font-size:13px;color:var(--green-dark);margin-top:4px}
  .award-circle{left:236px;top:170px;width:118px;height:118px;border-radius:50%;background:var(--purple);border:4px solid var(--green);display:flex;align-items:center;justify-content:center;text-align:center;color:var(--white);font-family:"Open Sans",sans-serif;font-weight:700;font-size:11px;line-height:1.25;padding:10px}
  .cover-photos{left:20px;top:390px}
  .banner{left:16px;top:585px;width:336px;background:var(--purple-deep);color:var(--white);text-align:center;font-family:"Open Sans",sans-serif;font-weight:700;font-size:15px;line-height:1.25;padding:10px 8px}
  .finalist{left:0;top:690px;width:368px;text-align:center;color:var(--white);font-family:"Open Sans",sans-serif;font-weight:700;font-size:16px;line-height:1.3}
</style>
</head>
<body>
<main class="brochure">

  <section class="panel panel-curriculum">
    <svg class="panel-bg" viewBox="0 0 368 780" aria-hidden="true">
      <rect width="368" height="780" fill="var(--purple)"/>
      <path d="M0 0H368V390Q190 440 0 430Z" fill="var(--white)"/>
      <path d="M0 430Q190 440 368 390V412Q190 462 0 452Z" fill="var(--green)"/>
      <path d="M0 765Q190 780 368 750V780H0Z" fill="var(--green)"/>
    </svg>
    <div class="abs quote-mark quote-open">“</div>
    <p class="abs quote-text">Passion is lifted from the earth itself by the muddy hands of the young; it travels along grass stained sleeves to the heart. If we are going to save environmentalism and the environment, we must also save an endangered indicator species: the child in nature.</p>
    <div class="abs quote-author">Marion Hale</div>
    <div class="abs quote-mark quote-close">”</div>
    <svg class="abs photo-pair" width="368" height="210" viewBox="0 0 368 210">
      <circle cx="245" cy="62" r="52" fill="#8fb6c9" stroke="var(--purple)" stroke-width="6" role="img" aria-label="Photo of the shaded outdoor play yard"/>
      <circle cx="110" cy="135" r="70" fill="#7d6a55" stroke="var(--green)" stroke-width="6" role="img" aria-label="Photo of children walking through the garden"/>
    </svg>
    <div class="abs curriculum">
      <h2 class="section-title">Our Curriculum</h2>
      <div class="title-rule"></div>
      <p>As your child grows older you will start to consider those all-important decisions of where to enrol them for Kindergarten, Pre-primary, primary school and eventually high school.</p>
      <p>School readiness has become increasingly important as educational expectations continue to rise. It is our belief that a comprehensive and holistic Kindergarten program is an essential part of a child's learning experience and essential when transitioning to school.</p>
      <p>At the core of our program is a Child-First Curriculum that is child centered and takes a 'hands on' approach, with educators who create a stimulating environment and experiences which are safe, nurturing and fun.</p>
    </div>
  </section>

  <section class="panel panel-contact">
    <svg class="panel-bg" viewBox="0 0 368 780" aria-hidden="true">
      <rect width="368" height="780" fill="var(--purple-dark)"/>
      <path d="M0 0H368V300Q190 360 0 340Z" fill="var(--grey-light)"/>
      <path d="M0 340Q190 360 368 300V325Q190 385 0 365Z" fill="var(--green)"/>
      <path d="M0 690Q190 705 368 660V700Q190 745 0 730Z" fill="var(--grey-dark)"/>
      <path d="M0 715Q190 730 368 685V780H0Z" fill="var(--green)"/>
    </svg>
    <div class="abs badges">
      <svg width="110" height="70" role="img" aria-label="Quality rating badge"><rect width="110" height="70" rx="6" fill="var(--badge-grey)"/></svg>
      <svg width="60" height="70" role="img" aria-label="Awards badge"><rect width="60" height="70" rx="6" fill="var(--badge-grey)"/></svg>
      <svg width="50" height="50" role="img" aria-label="Partner badge"><rect width="50" height="50" rx="6" fill="var(--badge-grey)"/></svg>
    </div>
    <p class="abs tagline">but if little things<br>big things grow</p>
    <div class="abs info">
      <h2>Opening Hours:</h2>
      <div class="rule"></div>
      <div class="hours">6:00am - 6:00pm Monday-Friday</div>
      <div class="small">(except public holidays)</div>
      <div class="line">
        <svg width="12" height="16" viewBox="0 0 12 16" aria-hidden="true"><path d="M6 0a6 6 0 0 1 6 6c0 4-6 10-6 10S0 10 0 6a6 6 0 0 1 6-6z" fill="var(--green)"/><circle cx="6" cy="6" r="2.2" fill="var(--purple-dark)"/></svg>
        18 Banksia Road,</div>
      <div class="line">Coral Bay, WA 6100</div>
      <div class="line" style="margin-top:6px"><span class="social-dot"></span>brightsproutsAU</div>
      <div class="enrol">ENROL NOW</div>
      <div class="phone">
        <svg width="18" height="18" viewBox="0 0 24 24" aria-hidden="true"><path d="M6.6 10.8a15 15 0 0 0 6.6 6.6l2.2-2.2a1 1 0 0 1 1-.25 11.4 11.4 0 0 0 3.6.6 1 1 0 0 1 1 1V20a1 1 0 0 1-1 1A17 17 0 0 1 3 4a1 1 0 0 1 1-1h3.5a1 1 0 0 1 1 1c0 1.25.2 2.45.6 3.6a1 1 0 0 1-.25 1z" fill="var(--green)"/></svg>
        (08) 9400 1287</div>
      <div class="email">
        <svg width="16" height="12" viewBox="0 0 16 12" aria-hidden="true"><rect x=".5" y=".5" width="15" height="11" fill="none" stroke="var(--green)"/><path d="M.5.5 8 7l7.5-6.5" fill="none" stroke="var(--green)"/></svg>
        hello@brightsprouts.com.au</div>
    </div>
    <div class="abs web">
      <svg width="16" height="16" viewBox="0 0 16 16" aria-hidden="true"><circle cx="8" cy="8" r="7" fill="none" stroke="var(--purple-dark)" stroke-width="1.5"/><path d="M1 8h14M8 1c-3 3.5-3 10.5 0 14M8 1c3 3.5 3 10.5 0 14" fill="none" stroke="var(--purple-dark)" stroke-width="1.2"/></svg>
      www.brightsprouts.com.au</div>
  </section>

  <section class="panel panel-cover">
    <svg class="panel-bg" viewBox="0 0 368 780" aria-hidden="true">
      <rect width="368" height="780" fill="var(--white)"/>
      <rect x="0" y="150" width="368" height="500" fill="#7a5a3e" role="img" aria-label="Photo of the outdoor play area with a mud kitchen"/>
      <path d="M0 0H368V120Q190 175 0 150Z" fill="var(--white)"/>
      <path d="M0 150Q190 175 368 120V140Q190 195 0 170Z" fill="var(--green)"/>
      <path d="M0 640H368V780H0Z" fill="var(--green)"/>
    </svg>
    <div class="abs brand">
      <div class="brand-name"><span class="brand-dot"></span>Bright Sprouts</div>
      <div class="brand-sub">Early Development &amp; Education Centre</div>
    </div>
    <div class="abs award-circle">WA State winner Early Childhood Director of the Year 2018</div>
    <svg class="abs cover-photos" width="240" height="180" viewBox="0 0 240 180">
      <circle cx="70" cy="70" r="60" fill="#5f6b48" stroke="var(--green)" stroke-width="5" role="img" aria-label="Photo of children playing at a sensory table"/>
      <circle cx="180" cy="60" r="52" fill="#6b5d72" stroke="var(--purple)" stroke-width="5" role="img" aria-label="Photo of a child exploring outdoors"/>
      <circle cx="140" cy="130" r="42" fill="#857a66" stroke="var(--purple)" stroke-width="5" role="img" aria-label="Photo of children building together"/>
    </svg>
    <div class="abs banner">Finalist, Early Childhood Service<br>of the Year, 2018, 2017 &amp; 2016</div>
    <div class="abs finalist">Finalist, Early Childhood Director<br>of the Year, 2016</div>
  </section>

</main>
</body>
</html>
```